Perfect — here’s the updated version of your description with **title #1** and the integration/booking functionality references removed, while still keeping the “motivation to book” idea in the design style:
---
**Luxury Property Website Design – Dominican Republic**
We are looking to create a professional and visually appealing **website design** for a premium property that we will be promoting as a short-term rental.
The property is located in an **exclusive area of the Dominican Republic** and offers a high-end experience for guests. Our goal is to create a website that highlights the **luxury, comfort, and exclusivity** of the property, while motivating visitors to **make a reservation inquiry**.
**Key Requirements:**
* A clean, modern, and elegant design that reflects the **premium nature** of the property.
* High-quality visual presentation of the **property’s best features** (rooms, amenities, location, views, nearby attractions).
* Easy-to-navigate structure
* Mobile-friendly and optimized for all screen sizes.
* Space for testimonials or guest reviews to build trust.
**Design Style We Like:**
* Elegant and sophisticated, with a touch of tropical luxury.
* Use of high-quality photography, subtle animations, and a warm color palette that reflects the Caribbean atmosphere.
* A premium feel, similar to boutique hotel or luxury villa rental websites.
**Deliverables:**
* Homepage design.
* Property detail page design (with gallery, amenities, and booking inquiry section).
Contact page or About Us page
* Photo Gallery
The final design should capture the essence of a **luxury getaway** and make visitors feel compelled to reserve their night.

```html
<!DOCTYPE html>
<html lang="en">
<head>
<meta charset="UTF-8">
<title>Marebella Villas – Luxury Property</title>
<link href="https://fonts.googleapis.com/css2?family=Anton&family=Nunito+Sans:wght@300;400&family=Poppins:wght@400;500;600&display=swap" rel="stylesheet">
<style>
:root{
  --navy:#0b3158;
  --navy-deep:#082746;
  --navy-soft:#16406a;
  --teal:#2fbcd5;
  --teal-light:#5bc8dc;
  --gold:#f1d77a;
  --white:#ffffff;
  --text:#2a2a2a;
}
*{margin:0;padding:0;box-sizing:border-box}
html,body{width:1200px;height:3389px;overflow:hidden}
body{position:relative;background:var(--white);font-family:"Nunito Sans",sans-serif;color:var(--text)}
.abs{position:absolute}
.display{font-family:"Anton",sans-serif;font-weight:400;letter-spacing:0}

/* hero */
.hero{left:0;top:0;width:1200px;height:658px;background:linear-gradient(180deg,#2c2f3d 0%,#4c4b57 30%,#3a3f3c 60%,#1d2a22 100%)}
.hero-wedge{left:0;top:0}
.brand{left:134px;top:44px;font-family:"Poppins",sans-serif;font-weight:600;font-size:30px;line-height:40px;color:var(--white)}
.nav{top:61px;font-family:"Poppins",sans-serif;font-size:14px;color:var(--white)}
.nav.active{color:var(--teal);font-weight:600}
.hero-frame{left:255px;top:225px;width:689px;height:307px;border:1px solid rgba(255,255,255,.35)}
.hero-title{left:255px;width:689px;top:262px;text-align:center;font-size:44px;line-height:48px;color:var(--white)}
.hero-text{left:380px;width:440px;top:385px;text-align:center;font-size:14.5px;line-height:19px;font-weight:300;color:var(--white)}
.btn{font-family:"Poppins",sans-serif;font-weight:600;color:var(--white);background:var(--navy);display:flex;align-items:center;justify-content:center}
.hero-btn{left:508px;top:463px;width:184px;height:41px;font-size:15px;border:2px solid var(--white)}
.scroll-line{left:1109px;top:205px;width:1px;height:134px;background:var(--white)}
.scroll-label{left:1092px;top:358px;transform:rotate(90deg);font-family:"Poppins",sans-serif;font-size:13px;color:var(--white)}

/* shared */
.ornament{width:122px;height:12px;border-radius:6px;background:linear-gradient(90deg,rgba(47,188,213,.2),var(--teal),rgba(47,188,213,.2))}
.section-title{font-size:60px;color:var(--navy);line-height:1}

/* about */
.about-title{left:149px;top:682px}
.about-orn{left:178px;top:749px}
.about-text{left:149px;top:780px;width:440px;font-size:13px;line-height:24px}
.about-text p+p{margin-top:24px}
.about-btn{left:153px;top:1011px;width:139px;height:38px;font-size:15px}
.frame-gold{border:1px solid var(--gold)}
.about-frame{left:617px;top:682px;width:436px;height:368px}
.about-photo{left:628px;top:694px;width:434px;height:368px;background:linear-gradient(135deg,#4aa8b8 0%,#7f9b74 45%,#e8e2d4 100%)}

/* features */
.features-title{left:0;width:1200px;top:1115px;text-align:center}
.center-orn{left:539px}
.feature-frame{width:286px;height:308px}
.feature{width:286px;height:308px}
.feature-label{left:462px;width:286px;top:1460px;text-align:center;font-family:"Poppins",sans-serif;font-size:29px;color:var(--white)}
.plus-box{left:582px;top:1388px;width:36px;height:36px;border:1px solid var(--white);color:var(--white);font-size:22px;display:flex;align-items:center;justify-content:center;font-family:"Poppins",sans-serif}

/* faq */
.faq-title{left:0;width:1200px;top:1951px;text-align:center}
.faq-box{left:138px;top:2085px;width:924px;height:492px;background:var(--navy)}
.faq-inner{left:147px;top:2094px;width:906px;height:472px;border:2px solid var(--white)}
.faq-photo{left:158px;top:2104px;width:399px;height:450px;background:linear-gradient(180deg,#5e8fc4 0%,#e9ecee 50%,#6fa4b9 100%)}
.faq-open{left:575px;top:2131px;width:457px;height:113px;background:var(--navy-soft)}
.faq-open-head{left:575px;top:2131px;width:457px;height:44px;background:var(--teal-light)}
.faq-q{font-family:"Poppins",sans-serif;font-weight:600;font-size:22px;color:var(--white);left:597px}
.faq-a{left:597px;top:2186px;width:428px;font-size:12px;line-height:19px;color:var(--white)}
.faq-row{left:575px;width:457px;height:1px;background:rgba(255,255,255,.75)}
.chev{left:995px}

/* testimonials */
.testimonials{left:0;top:2656px;width:1200px;height:463px;background:linear-gradient(180deg,#33c1d9,#2ab3cd)}
.testi-title{left:0;width:1200px;top:2717px;text-align:center;color:var(--white)}
.quote-badge{left:568px;top:2854px;width:64px;height:64px;border-radius:50%;background:var(--navy)}
.quote-text{left:180px;width:840px;top:2940px;text-align:center;font-size:21.5px;line-height:25px;color:var(--white);font-weight:300}
.quote-name{left:0;width:1242px;top:3032px;text-align:center;font-family:"Poppins",sans-serif;font-weight:600;font-size:20px;color:var(--white)}
.arrow{width:44px;height:44px;border-radius:50%;background:var(--white);top:2936px}

/* footer */
.footer{left:0;top:3119px;width:1200px;height:270px;background:var(--navy-deep)}
.footer-brand{left:0;width:1200px;top:3166px;text-align:center;font-family:"Poppins",sans-serif;font-size:32px;color:var(--white);font-weight:400}
.footer-nav{top:3231px;font-family:"Poppins",sans-serif;font-size:14.5px;color:var(--white)}
.footer-nav.active{font-weight:600}
.social{top:3283px;width:16px;height:16px;border-radius:50%;border:1.5px solid var(--white)}
.copyright{left:0;width:1200px;top:3333px;text-align:center;font-family:"Poppins",sans-serif;font-size:14.5px;color:var(--white)}
</style>
</head>
<body>

<!-- HERO -->
<div class="abs hero" role="img" aria-label="Modern curved luxury villa on a hillside at dusk"></div>
<svg class="abs hero-wedge" width="1200" height="670" viewBox="0 0 1200 670">
  <polygon points="0,658 599,608 1200,555 1200,658" fill="#ffffff"/>
  <polygon points="599,608 1200,555 1200,658" fill="#2fbcd5"/>
</svg>
<div class="abs brand">Marebella Villas</div>
<div class="abs nav active" style="left:508px">Home</div>
<div class="abs nav" style="left:583px">About Us</div>
<div class="abs nav" style="left:679px">Property</div>
<div class="abs nav" style="left:772px">Photo Gallery</div>
<div class="abs nav" style="left:897px">Contact Us</div>
<div class="abs hero-frame"></div>
<h1 class="abs hero-title display">Where Dominican Elegance<br>Meets Digital Brilliance</h1>
<p class="abs hero-text">We craft world-class luxury real estate websites that capture the beauty, prestige, and lifestyle of the Dominican Republic’s most coveted properties.</p>
<div class="abs btn hero-btn">Book an Inquiry</div>
<div class="abs scroll-line"></div>
<div class="abs scroll-label">Scroll</div>

<!-- ABOUT -->
<h2 class="abs section-title display about-title">About Us</h2>
<div class="abs ornament about-orn" role="img" aria-label="Decorative scroll ornament"></div>
<div class="abs about-text">
  <p>we specialize in designing bespoke websites for luxury villas, beachfront estates, and upscale developments across the Dominican Republic. Our team combines refined aesthetics with cutting-edge technology to create elegant online experiences that elevate your brand and attract high-net-worth buyers from around the world.</p>
  <p>From Punta Cana to Bahía Serena, Sosúa to Las Terrenas – we understand the luxury market and know how to showcase your properties with sophistication and impact</p>
</div>
<div class="abs btn about-btn">Read more</div>
<div class="abs frame-gold about-frame"></div>
<div class="abs about-photo" role="img" aria-label="Aerial view of a beachfront resort with pools and palm trees"></div>

<!-- FEATURES -->
<h2 class="abs section-title display features-title">Features</h2>
<div class="abs ornament center-orn" style="top:1199px" role="img" aria-label="Decorative scroll ornament"></div>

<div class="abs frame-gold feature-frame" style="left:147px;top:1249px"></div>
<div class="abs feature" style="left:154px;top:1255px;background:linear-gradient(180deg,#3b8ed8 0%,#e46aa6 55%,#f0d8b4 100%)" role="img" aria-label="Colorful beach cabanas under palm trees"></div>
<div class="abs frame-gold feature-frame" style="left:455px;top:1246px"></div>
<div class="abs feature" style="left:462px;top:1253px;background:linear-gradient(180deg,#2f6ea8 0%,#5d93a8 50%,#1aa7b4 100%)" role="img" aria-label="Resort pool lined with palm trees"></div>
<div class="abs plus-box">+</div>
<div class="abs feature-label">Amenities</div>
<div class="abs frame-gold feature-frame" style="left:760px;top:1246px"></div>
<div class="abs feature" style="left:767px;top:1253px;background:linear-gradient(180deg,#3e4a7c 0%,#2b5b6a 50%,#17a6c4 80%,#2a3a25 100%)" role="img" aria-label="Modern villa with illuminated pool at night"></div>

<div class="abs frame-gold feature-frame" style="left:147px;top:1580px"></div>
<div class="abs feature" style="left:154px;top:1587px;background:linear-gradient(135deg,#6c8c3c 0%,#e9e4d6 45%,#8a4a26 75%,#e8b04c 100%)" role="img" aria-label="Plate of rice, stewed chicken, avocado and plantains"></div>
<div class="abs frame-gold feature-frame" style="left:455px;top:1578px"></div>
<div class="abs feature" style="left:462px;top:1585px;background:linear-gradient(180deg,#e4e6e8 0%,#c8b59a 45%,#3ab8c0 100%)" role="img" aria-label="White villa bedroom opening onto a pool"></div>
<div class="abs frame-gold feature-frame" style="left:760px;top:1578px"></div>
<div class="abs feature" style="left:767px;top:1585px;background:linear-gradient(180deg,#f2f4f6 0%,#7fc6e4 45%,#eef0f2 100%)" role="img" aria-label="Bright living room with ocean views"></div>

<!-- FAQ -->
<h2 class="abs section-title display faq-title">FAQ</h2>
<div class="abs ornament center-orn" style="top:2027px" role="img" aria-label="Decorative scroll ornament"></div>
<div class="abs faq-box"></div>
<div class="abs faq-inner"></div>
<div class="abs faq-photo" role="img" aria-label="Terraced white villa with lounge deck and pool"></div>

<div class="abs faq-open"></div>
<div class="abs faq-open-head"></div>
<div class="abs faq-q" style="top:2136px">Lorem ipsum dolor sit amet ?</div>
<svg class="abs chev" style="top:2147px" width="14" height="10" viewBox="0 0 14 10"><polyline points="3,7 7,3 11,7" fill="none" stroke="#fff" stroke-width="1.6"/></svg>
<p class="abs faq-a">Lorem ipsum dolor sit amet, consectetur adipiscing elit, sed do eiusmod tempor incididunt ut labore et dolore magna aliqua.</p>

<div class="abs faq-q" style="top:2264px">Lorem ipsum dolor sit amet ?</div>
<svg class="abs chev" style="top:2274px" width="14" height="10" viewBox="0 0 14 10"><polyline points="3,3 7,7 11,3" fill="none" stroke="#fff" stroke-width="1.6"/></svg>
<div class="abs faq-row" style="top:2305px"></div>
<div class="abs faq-q" style="top:2313px">Lorem ipsum dolor sit amet ?</div>
<svg class="abs chev" style="top:2323px" width="14" height="10" viewBox="0 0 14 10"><polyline points="3,3 7,7 11,3" fill="none" stroke="#fff" stroke-width="1.6"/></svg>
<div class="abs faq-row" style="top:2354px"></div>
<div class="abs faq-q" style="top:2366px">Lorem ipsum dolor sit amet ?</div>
<svg class="abs chev" style="top:2376px" width="14" height="10" viewBox="0 0 14 10"><polyline points="3,3 7,7 11,3" fill="none" stroke="#fff" stroke-width="1.6"/></svg>
<div class="abs faq-row" style="top:2403px"></div>
<div class="abs faq-q" style="top:2413px">Lorem ipsum dolor sit amet ?</div>
<svg class="abs chev" style="top:2423px" width="14" height="10" viewBox="0 0 14 10"><polyline points="3,3 7,7 11,3" fill="none" stroke="#fff" stroke-width="1.6"/></svg>
<div class="abs faq-row" style="top:2452px"></div>
<div class="abs faq-q" style="top:2462px">Lorem ipsum dolor sit amet ?</div>
<svg class="abs chev" style="top:2472px" width="14" height="10" viewBox="0 0 14 10"><polyline points="3,3 7,7 11,3" fill="none" stroke="#fff" stroke-width="1.6"/></svg>
<div class="abs faq-row" style="top:2500px"></div>

<!-- TESTIMONIALS -->
<div class="abs testimonials" role="img" aria-label="Faint tropical villa backdrop in turquoise"></div>
<h2 class="abs section-title display testi-title">Testimonials</h2>
<div class="abs ornament center-orn" style="top:2801px;background:linear-gradient(90deg,rgba(255,255,255,.3),#fff,rgba(255,255,255,.3))" role="img" aria-label="Decorative scroll ornament"></div>
<div class="abs quote-badge"></div>
<svg class="abs" style="left:583px;top:2874px" width="34" height="22" viewBox="0 0 34 22">
  <path d="M2 20 V11 Q2 3 9 2 V6 Q6 7 6 11 H10 V20 Z M17 20 V11 Q17 3 24 2 V6 Q21 7 21 11 H25 V20 Z" fill="#fff"/>
</svg>
<p class="abs quote-text">“Lorem ipsum dolor sit amet, consectetur adipiscing elit, sed do eiusmod tempor incididunt ut labore et dolore magna aliqua. Quis ipsum suspendisse ultrices gravida. Risus commodo viverra maecenas accumsan lacus vel facilisis. “</p>
<div class="abs quote-name">-Elena Marsh</div>
<div class="abs arrow" style="left:83px"></div>
<svg class="abs" style="left:99px;top:2950px" width="12" height="16" viewBox="0 0 12 16"><polyline points="9,2 3,8 9,14" fill="none" stroke="#0b3158" stroke-width="2"/></svg>
<div class="abs arrow" style="left:1115px"></div>
<svg class="abs" style="left:1132px;top:2950px" width="12" height="16" viewBox="0 0 12 16"><polyline points="3,2 9,8 3,14" fill="none" stroke="#0b3158" stroke-width="2"/></svg>

<!-- FOOTER -->
<div class="abs footer"></div>
<div class="abs footer-brand">Marebella Villas</div>
<div class="abs footer-nav active" style="left:356px">Home</div>
<div class="abs footer-nav" style="left:435px">About Us</div>
<div class="abs footer-nav" style="left:536px">Property</div>
<div class="abs footer-nav" style="left:632px">Photo Gallery</div>
<div class="abs footer-nav" style="left:763px">Contact Us</div>
<div class="abs social" style="left:521px"></div>
<div class="abs social" style="left:566px"></div>
<div class="abs social" style="left:611px"></div>
<div class="abs social" style="left:658px"></div>
<div class="abs copyright">© 2025 | www.marebellavillas-example.com</div>

</body>
</html>
```